Bright Path Flyer Design for Virtual Online Clinic. -5.5 x 8.5 inches (half sheet)

We need a clean, modern flyer design for Bright Path, a new virtual walk-in clinic based in British Columbia. The flyer will be used in libraries, pharmacies, and community centers to help residents easily access primary care through their Bright Path NFC access card.
The flyer will ask a question : NEED A DOCTOR? This should be large and attention grabbing.
The design should clearly feature a Bright Path card image (the access card) as the centerpiece and visually show how patients can use it to book appointments. The tone should feel trustworthy, healthcare-oriented, and community-friendly — clean fonts, clear spacing, and strong readability from a distance.

Side One: This card has the NFC Access Card.
NEED A DOCTOR? (Large Font, Attention Grabbing)
How to Book an Appointment using your Bright Path Card
Step 1: Tap Your Card on Your Phone
Hold your card near the back of your phone.
It will activate automatically — no app needed.
The Bright Path scheduler will open.
Step 2: Schedule Your Appointment
Select your clinical concern.
Choose your time window.
Register (only once).
Confirm your appointment.
Step 3: Relax, we’ll take care of the rest
A doctor will call during your scheduled time.
Once booked, you’ll be able to call our office.
No emails, no texts — just a real person.
It’s that simple.
Side Two:
About Bright Path
Created by Dr. Marcus Ferrigan
Bright Path was founded to make healthcare simple and convenient. Prescription renewals. Common infections. Medical notes. And so much more.
Our doctors can address 120+ health concerns virtually — providing quality care without the waiting room. No waiting rooms. Just real doctors providing real care.
Why Patients Choose Bright Path
Easy access – book and be seen from anywhere in BC.
Effortless booking – tap your Bright Path Card to begin.
Trusted physicians – every visit is with a licensed BC family doctor.
How It Works
Book your visit — choose a time window that fits your day.
Join the queue — you’ll be called when it’s your turn.
Speak directly with your doctor — simple, secure, and stress-free.
Convenient Care for Common Concerns

Additional Details.
Please find the domain to be launched soon. I've attached the NFC card file for review, it is 85.5 mm x 54 mm. The card will be glued to the flyer.
I've attached examples of flyers but they are not the look I am seeking and I am looking for creative solutions.
Thank you!
http://brightpath-example.test/

Adult Patients in British Columbia

Healthcare

• Looking for clean lines, uniform appearance, and high legibility i.e poppins

0054AA
0677BA
7BADD7
CADEEF
E8F1F8

• Need A Doctor?
• Elegant style, not too busy, clear layout.
• Clutter, look cheap - review examples.

```html
<!DOCTYPE html>
<html lang="en">
<head>
<meta charset="utf-8">
<title>Bright Path Flyer</title>
<link href="https://fonts.googleapis.com/css2?family=Poppins:wght@500;600;700;800&family=Roboto:wght@400;500&display=swap" rel="stylesheet">
<style>
  :root{
    --backdrop:#8f8f8f;
    --navy:#223f96;
    --blue:#0054AA;
    --mid:#0677BA;
    --sky:#7BADD7;
    --pale:#CADEEF;
    --mist:#E8F1F8;
    --ink:#1d1d1f;
    --body:#3a3a3a;
    --white:#ffffff;
  }
  *{box-sizing:border-box;margin:0;padding:0}
  html,body{width:1200px;height:965px;overflow:hidden;background:var(--backdrop)}
  body{position:relative;font-family:"Roboto",Arial,sans-serif;color:var(--ink)}
  .page{position:absolute;top:112px;width:480px;height:742px;overflow:hidden;background:var(--white);box-shadow:0 6px 22px rgba(0,0,0,.28)}
  .page--front{left:96px}
  .page--back{left:625px;background:var(--navy)}
  .abs{position:absolute}

  /* front */
  .front-header{left:0;top:0;width:480px;height:276px;background:var(--mist)}
  .front-header svg{position:absolute;left:0;top:0}
  .brand-name{font-family:"Poppins",sans-serif;font-weight:600;color:var(--white);font-size:34px;left:0;width:480px;text-align:center;top:52px;letter-spacing:.5px}
  .headline{font-family:"Poppins",sans-serif;font-weight:800;color:var(--navy);font-size:41px;left:0;width:480px;text-align:center;top:150px;letter-spacing:-.5px}
  .headline-rule{left:63px;top:208px;width:354px;height:2px;background:var(--navy)}
  .subtitle{left:0;width:480px;text-align:center;top:226px;font-size:16px;color:var(--ink)}
  .front-art{left:0;top:276px}

  .access-card{position:absolute;border:1.5px solid var(--white);box-shadow:0 4px 12px rgba(0,0,0,.3);overflow:hidden}
  .access-card--front{background:var(--navy)}
  .access-card--back{background:var(--white)}
  .card-name{position:absolute;left:0;width:100%;text-align:center;font-family:"Poppins",sans-serif;font-weight:600;color:var(--white)}
  .card-url{position:absolute;left:0;width:100%;text-align:center;color:var(--white);font-size:5.5px}
  .card-band{position:absolute;left:0;top:0;bottom:0;background:var(--navy)}
  .card-back-name{position:absolute;font-family:"Poppins",sans-serif;font-weight:600;color:var(--navy)}
  .card-tap{position:absolute;color:var(--blue);font-size:5.5px;display:flex;align-items:center;gap:3px}
  .card-tap span.chip{display:inline-block;width:11px;height:7px;border:1px solid var(--blue);border-radius:2px}
  .nfc-square{position:absolute;width:8px;height:8px;background:var(--navy)}

  .step-icon{position:absolute;left:253px;width:44px;height:44px;border-radius:50%;background:var(--blue);display:flex;align-items:center;justify-content:center}
  .step-title{position:absolute;left:310px;font-size:13px;line-height:18px;color:var(--ink);font-weight:500}
  .step-body{position:absolute;left:310px;font-size:10px;line-height:15.3px;color:var(--ink);text-align:justify}

  /* back */
  .back-panel{left:19px;top:23px;width:431px;height:695px;background:linear-gradient(to bottom,var(--white) 0,var(--white) 72%,#e6eef6 86%,#cfdce8 100%)}
  .about-title{left:56px;top:52px;font-family:"Poppins",sans-serif;font-weight:800;font-size:27px;color:var(--navy);letter-spacing:.2px}
  .rule{height:2px;background:var(--navy)}
  .created{left:56px;top:111px;font-size:15.5px;color:var(--ink)}
  .about-text{left:56px;top:140px;width:348px;font-size:11.3px;line-height:16.9px;color:var(--body);text-align:justify}
  .about-text p+p{margin-top:0}
  .col-head{font-family:"Poppins",sans-serif;font-weight:700;font-size:14.5px;color:var(--blue);letter-spacing:.2px}
  .tick{position:absolute;left:56px;width:26px;height:26px;border-radius:50%;display:flex;align-items:center;justify-content:center}
  .tick--light{background:var(--sky)}
  .tick--dark{background:var(--blue)}
  .num{position:absolute;left:270px;width:26px;height:26px;border-radius:50%;display:flex;align-items:center;justify-content:center;color:var(--white);font-family:"Poppins",sans-serif;font-size:11.5px;font-weight:500}
  .num--dark{background:var(--blue)}
  .num--light{background:var(--sky)}
  .item-title{position:absolute;font-size:12.6px;line-height:17px;color:var(--ink);font-weight:500}
  .item-body{position:absolute;font-size:10px;line-height:15.2px;color:var(--body)}
  .concerns-band{left:55px;top:553px;width:370px;height:26px;background:var(--sky);border-radius:2px;color:var(--white);font-size:15.5px;font-weight:500;display:flex;align-items:center;justify-content:center}
</style>
</head>
<body>

<!-- FRONT SIDE -->
<section class="page page--front">
  <header class="abs front-header">
    <svg width="480" height="276" viewBox="0 0 480 276" role="img" aria-label="Dark blue arch with a faint bird pattern">
      <path d="M0 0 H480 Q440 129 240 129 Q40 129 0 0 Z" fill="var(--navy)"/>
    </svg>
    <div class="abs brand-name">Bright Path</div>
    <h1 class="abs headline">NEED A DOCTOR?</h1>
    <div class="abs headline-rule"></div>
    <p class="abs subtitle">How to Book an Appointment using your Bright Path Card</p>
  </header>

  <svg class="abs front-art" width="480" height="466" viewBox="0 0 480 466" role="img" aria-label="Blue patterned backdrop with a large white bird silhouette">
    <path d="M0 0 H272 L150 150 L120 260 L104 466 H0 Z" fill="var(--navy)"/>
    <path d="M150 0 L75 160 L60 240 L0 270 L0 300 L48 290 L100 170 Z" fill="var(--white)" opacity="0"/>
  </svg>

  <div class="access-card access-card--front" style="left:37px;top:424px;width:203px;height:114px" role="img" aria-label="Bright Path access card, front">
    <div class="card-name" style="top:40px;font-size:19px">Bright Path</div>
    <div class="card-url" style="top:70px">www.brightpath-example.test</div>
  </div>
  <div class="access-card access-card--back" style="left:37px;top:549px;width:203px;height:114px" role="img" aria-label="Bright Path access card, back with tap area">
    <div class="card-band" style="width:58px"></div>
    <div class="nfc-square" style="right:8px;top:10px"></div>
    <div class="card-back-name" style="left:74px;top:40px;font-size:18px">Bright Path</div>
    <div class="card-tap" style="right:9px;bottom:10px">Tap Here to Book <span class="chip"></span></div>
  </div>

  <div class="step-icon" style="top:317px">
    <svg width="24" height="24" viewBox="0 0 24 24" fill="none" stroke="#fff" stroke-width="1.5"><rect x="6" y="2" width="11" height="19" rx="2"/><path d="M10 18h3"/></svg>
  </div>
  <div class="step-title" style="top:322px;width:140px">Tap Your Card on<br>Your Phone</div>
  <p class="step-body" style="top:362px;width:126px">Hold your card near the back of your phone.It will activate automatically — no app needed.The Bright Path scheduler will open.</p>

  <div class="step-icon" style="top:459px">
    <svg width="24" height="24" viewBox="0 0 24 24" fill="none" stroke="#fff" stroke-width="1.4"><rect x="3" y="5" width="18" height="15" rx="2"/><path d="M3 9h18M8 3v4M16 3v4"/><path d="M7 13h2M11 13h2M7 16h2M11 16h2"/><circle cx="17" cy="16" r="2.6"/></svg>
  </div>
  <div class="step-title" style="top:463px;width:140px">Schedule Your<br>Appointment</div>
  <p class="step-body" style="top:506px;width:150px;text-align:left">Select your clinical concern.<br>Choose your time window.<br>Register (only once).<br>Confirm your appointment.</p>

  <div class="step-icon" style="top:584px">
    <svg width="24" height="24" viewBox="0 0 24 24" fill="none" stroke="#fff" stroke-width="1.4"><circle cx="12" cy="5" r="2.4"/><path d="M12 8v6M7 12l5 2 5-2M5 19c2-3 12-3 14 0M4 21h16"/></svg>
  </div>
  <div class="step-title" style="top:591px;width:150px">Relax, we’ll take care<br>of the rest</div>
  <p class="step-body" style="top:634px;width:147px">A doctor will call during your scheduled time.Once booked, you’ll be able to call our office.No emails, no texts — just a real person.It’s that simple.</p>
</section>

<!-- BACK SIDE -->
<section class="page page--back">
  <div class="abs back-panel"></div>

  <h2 class="abs about-title">ABOUT BRIGHT PATH</h2>
  <div class="abs rule" style="left:56px;top:94px;width:272px"></div>
  <p class="abs created">Created by Dr. Marcus Ferrigan</p>
  <div class="abs about-text">
    <p>Bright Path was founded to make healthcare simple and convenient. Prescription renewals. Common infections. Medical notes. And so much more.</p>
    <p>Our doctors can address 120+ health concerns virtually — providing quality care without the waiting room. No waiting rooms. Just real doctors providing real care.</p>
  </div>

  <h3 class="abs col-head" style="left:56px;top:272px">WHY PATIENTS</h3>
  <div class="abs rule" style="left:56px;top:297px;width:172px"></div>
  <h3 class="abs col-head" style="left:56px;top:302px">CHOOSE BRIGHT PATH</h3>

  <h3 class="abs col-head" style="left:270px;top:272px">HOW IT WORKS</h3>
  <div class="abs rule" style="left:270px;top:297px;width:126px"></div>

  <div class="tick tick--light" style="top:347px"><svg width="12" height="12" viewBox="0 0 12 12" fill="none" stroke="#fff" stroke-width="1.6"><path d="M2 6.5l2.6 2.5L10 3.5"/></svg></div>
  <div class="item-title" style="left:93px;top:351px">Easy access</div>
  <p class="item-body" style="left:94px;top:372px;width:122px;text-align:justify">Book and be seen from anywhere in BC.</p>

  <div class="tick tick--dark" style="top:412px"><svg width="12" height="12" viewBox="0 0 12 12" fill="none" stroke="#fff" stroke-width="1.6"><path d="M2 6.5l2.6 2.5L10 3.5"/></svg></div>
  <div class="item-title" style="left:94px;top:416px">Trusted physicians</div>
  <p class="item-body" style="left:94px;top:440px;width:135px">Every visit is with a licensed BC family doctor.</p>

  <div class="tick tick--light" style="top:480px"><svg width="12" height="12" viewBox="0 0 12 12" fill="none" stroke="#fff" stroke-width="1.6"><path d="M2 6.5l2.6 2.5L10 3.5"/></svg></div>
  <div class="item-title" style="left:93px;top:484px">Effortless booking</div>
  <p class="item-body" style="left:94px;top:507px;width:135px">Tap your Bright Path Card to begin.</p>

  <div class="num num--dark" style="top:325px">01</div>
  <div class="item-title" style="left:308px;top:329px">Book your visit</div>
  <p class="item-body" style="left:308px;top:351px;width:115px">Choose a time window that fits your day.</p>

  <div class="num num--light" style="top:401px">02</div>
  <div class="item-title" style="left:308px;top:404px">Join the queue</div>
  <p class="item-body" style="left:308px;top:427px;width:115px">You’ll be called when it’s your turn.</p>

  <div class="num num--dark" style="top:476px">03</div>
  <div class="item-title" style="left:308px;top:479px;width:118px">Speak directly with your doctor</div>
  <p class="item-body" style="left:308px;top:518px;width:115px">Simple, secure, and stress-free.</p>

  <div class="abs concerns-band">Convenient Care for Common Concerns</div>

  <div class="access-card access-card--front" style="left:50px;top:591px;width:184px;height:103px" role="img" aria-label="Bright Path access card, front">
    <div class="card-name" style="top:36px;font-size:17px">Bright Path</div>
    <div class="card-url" style="top:64px">www.brightpath-example.test</div>
  </div>
  <div class="access-card access-card--back" style="left:247px;top:591px;width:183px;height:103px" role="img" aria-label="Bright Path access card, back with tap area">
    <div class="card-band" style="width:52px"></div>
    <div class="nfc-square" style="right:8px;top:9px"></div>
    <div class="card-back-name" style="left:66px;top:36px;font-size:16px">Bright Path</div>
    <div class="card-tap" style="right:8px;bottom:9px">Tap Here to Book <span class="chip"></span></div>
  </div>
</section>

</body>
</html>
```